I need a simple infographic that describes the 4 basic elements of how to effectively create change.

The overall title (Gentle Pressure Relentlessly Applied) should be at the top of the infographic. Subtitle is: "Leading Change".
There are four steps:
1. Alignment- Agreement on Approach
2. Transparency- Metrics for Assurance
3. Skills- Training and Coaching
4. Integrity- Culture of Accountability

Target Market(s)

Business Leaders in a training workshop

Font styles to use
Serif

Requirements
Must have
• Here are the 4 elements of the Infographic: Please show them in order.
• 1. Agreement on Approach. (Alignment)
• 2. Metrics for Assurance (Transparency)
• 3. Training and Coaching (Skills)
• 4. Culture of Accountability (Integrity)
Nice to have
• Cool Graphics that depict the 4 steps.
Should not have
• Pictures.

```html
<!DOCTYPE html>
<html lang="en">
<head>
<meta charset="utf-8">
<title>Gentle Pressure Relentlessly Applied – Leading Change</title>
<link rel="stylesheet" href="https://fonts.googleapis.com/css2?family=Montserrat:wght@400;700;800&display=swap">
<style>
  :root {
    --brand-blue: #00a8e4;
    --page-bg: #f4f5f6;
    --ring-grey: #c9cdd2;
    --white: #ffffff;
  }
  html, body {
    margin: 0;
    width: 1200px;
    height: 1200px;
    overflow: hidden;
    background: var(--page-bg);
  }
  .poster {
    position: absolute;
    left: 156px;
    top: 20px;
    width: 888px;
    height: 1160px;
    display: block;
    font-family: "Montserrat", Arial, sans-serif;
  }
  .title { fill: var(--brand-blue); font-weight: 800; font-size: 56px; letter-spacing: 1px; }
  .subtitle { fill: var(--brand-blue); font-weight: 400; font-size: 27px; letter-spacing: 2px; }
  .step-name { fill: var(--brand-blue); font-weight: 800; font-size: 26px; letter-spacing: 1px; }
  .step-desc { fill: var(--brand-blue); font-weight: 400; font-size: 21px; letter-spacing: 1px; }
  .brand-name { fill: var(--white); font-weight: 400; font-size: 22px; letter-spacing: 0.5px; }
  .arc { fill: none; stroke: var(--brand-blue); stroke-width: 11; stroke-linecap: round; }
  .connector { stroke: var(--brand-blue); stroke-width: 4; }
  .guide-ring { fill: none; stroke: var(--ring-grey); stroke-width: 1.2; stroke-dasharray: 3 4; }
  .badge-outer { fill: var(--white); stroke: var(--brand-blue); stroke-width: 7; }
  .badge-inner { fill: var(--brand-blue); }
  .icon-line { stroke: var(--white); stroke-width: 4; fill: none; }
</style>
</head>
<body>
<svg class="poster" viewBox="0 0 945 1235" xmlns="http://www.w3.org/2000/svg">
  <defs>
    <linearGradient id="poster-bg" x1="0" y1="0" x2="1" y2="1">
      <stop offset="0" stop-color="#dde1e5"/>
      <stop offset="0.55" stop-color="#eceef0"/>
      <stop offset="1" stop-color="#f7f8f9"/>
    </linearGradient>
  </defs>

  <!-- background -->
  <rect class="poster-bg" width="945" height="1235" fill="url(#poster-bg)"/>
  <path class="swoosh" d="M260 0 C150 180 60 330 0 470 L0 0 Z" fill="#f1f2f4" opacity="0.8"/>
  <path class="swoosh" d="M945 420 C700 560 420 620 0 760 L0 1235 L945 1235 Z" fill="#f3f4f6" opacity="0.7"/>
  <path class="base-band" d="M0 1068 C300 1045 650 1045 945 1090 L945 1235 L0 1235 Z" fill="var(--white)"/>

  <!-- heading -->
  <text class="title" x="475" y="105" text-anchor="middle">GENTLE PRESSURE</text>
  <text class="title" x="475" y="163" text-anchor="middle">RELENTLESSLY APPLIED</text>
  <line x1="283" y1="179" x2="625" y2="179" stroke="var(--brand-blue)" stroke-width="2"/>
  <text class="subtitle" x="460" y="213" text-anchor="middle">LEADING CHANGE</text>

  <!-- guide rings -->
  <circle class="guide-ring" cx="403" cy="595" r="297"/>
  <circle class="guide-ring" cx="403" cy="595" r="273"/>
  <circle class="guide-ring" cx="403" cy="595" r="250"/>
  <circle class="guide-ring" cx="403" cy="595" r="227"/>

  <!-- progress arcs -->
  <path class="arc" d="M403 298 A297 297 0 0 1 700 595"/>
  <path class="arc" d="M403 322 A273 273 0 0 1 596 788"/>
  <path class="arc" d="M403 345 A250 250 0 0 1 403 845"/>
  <path class="arc" d="M403 368 A227 227 0 1 1 242.5 755.5"/>

  <!-- centre hub -->
  <circle cx="403" cy="595" r="190" fill="#ededee"/>
  <circle cx="403" cy="595" r="172" fill="none" stroke="var(--brand-blue)" stroke-width="12"/>
  <circle cx="403" cy="595" r="150" fill="var(--brand-blue)"/>

  <!-- connectors -->
  <line class="connector" x1="700" y1="595" x2="756" y2="595"/>
  <line class="connector" x1="596" y1="788" x2="640" y2="833"/>
  <line class="connector" x1="403" y1="845" x2="403" y2="906"/>
  <line class="connector" x1="242" y1="756" x2="197" y2="798"/>

  <!-- step 1: alignment -->
  <g class="step step-alignment">
    <circle class="badge-outer" cx="800" cy="592" r="41"/>
    <circle class="badge-inner" cx="800" cy="592" r="31"/>
    <line class="icon-line" x1="783" y1="579" x2="817" y2="579"/>
    <line class="icon-line" x1="783" y1="588" x2="817" y2="588"/>
    <line class="icon-line" x1="783" y1="597" x2="817" y2="597"/>
    <line class="icon-line" x1="783" y1="606" x2="817" y2="606"/>
    <text class="step-name" x="805" y="667" text-anchor="middle">ALIGNMENT</text>
    <text class="step-desc" x="805" y="695" text-anchor="middle">AGREEMENT ON</text>
    <text class="step-desc" x="805" y="721" text-anchor="middle">APPROACH</text>
  </g>

  <!-- step 2: transparency -->
  <g class="step step-transparency">
    <circle class="badge-outer" cx="667" cy="860" r="41"/>
    <circle class="badge-inner" cx="667" cy="860" r="31"/>
    <rect x="651" y="864" width="5" height="12" fill="var(--white)"/>
    <rect x="659" y="858" width="5" height="18" fill="var(--white)"/>
    <circle cx="671" cy="853" r="10" fill="none" stroke="var(--white)" stroke-width="3"/>
    <line x1="678" y1="860" x2="686" y2="869" stroke="var(--white)" stroke-width="4" stroke-linecap="round"/>
    <text class="step-name" x="671" y="938" text-anchor="middle">TRANSPARENCY</text>
    <text class="step-desc" x="671" y="966" text-anchor="middle">METRICS FOR</text>
    <text class="step-desc" x="671" y="994" text-anchor="middle">ASSURANCE</text>
  </g>

  <!-- step 3: skills -->
  <g class="step step-skills">
    <circle class="badge-outer" cx="400" cy="950" r="41"/>
    <circle class="badge-inner" cx="400" cy="950" r="31" role="img" aria-label="Icon of a coach presenting at a board"/>
    <text class="step-name" x="400" y="1027" text-anchor="middle">SKILLS</text>
    <text class="step-desc" x="400" y="1055" text-anchor="middle">TRAINING AND</text>
    <text class="step-desc" x="400" y="1083" text-anchor="middle">COACHING</text>
  </g>

  <!-- step 4: integrity -->
  <g class="step step-integrity">
    <circle class="badge-outer" cx="165" cy="827" r="41"/>
    <circle class="badge-inner" cx="165" cy="827" r="31"/>
    <path d="M165 810 A17 17 0 1 0 182 827 L165 827 Z" fill="var(--white)"/>
    <path d="M169 823 L169 806 A17 17 0 0 1 186 823 Z" fill="var(--white)"/>
    <text class="step-name" x="163" y="905" text-anchor="middle">INTEGRITY</text>
    <text class="step-desc" x="163" y="933" text-anchor="middle">CULTURE OF</text>
    <text class="step-desc" x="163" y="962" text-anchor="middle">ACCOUNTABILITY</text>
  </g>

  <!-- footer brand band -->
  <path class="brand-band" d="M545 1125 L945 1125 L945 1235 L470 1235 C490 1180 505 1125 545 1125 Z" fill="var(--brand-blue)"/>
  <circle cx="590" cy="1178" r="22" fill="none" stroke="var(--white)" stroke-width="3"/>
  <text class="brand-name" x="624" y="1186" textLength="290" lengthAdjust="spacingAndGlyphs">NORTHWELL PARTNERS</text>
</svg>
</body>
</html>
```